Cruise price comparison web design project

The project's name is Wellenfuchsportal.
www.wellenfuchsportal.de
The current design (which I don't really like) can be found here:
http://wfp02.wellenfuchsportal.de/

I m not too happy with what the current developers have been done so far (in terms of design), so I hope to find a great designer her to develop a design that kicks arses. : )

We are currently developing a site for the German market that brings travel agents and cruise holiday makers together. We are not an ordinary travel agency.
Wellenfuchsportal is a quick and convenient way to have independent travel agencies compete to offer our site visitors the best cruise deal available in Europe.

Here is a short video that explains what one of our competitors does; it gives a good overview as our site will be similar:
http://www.voyabidder.com/video_how_voyabidder_works.php
(Voyabidder.com is not a great website in terms of design, so please dont get me wrong.)

The logo has already been created, but both the colours (should remain blueish) and the font can be modified. The font colour can be changed dramatically if you think this is of advantage.

The Website design should be professional and unique and become an eye catcher. It must attract visitors of all age groups, a "wow-effect" is definitely a bonus.
Users should easily see what this website is about.

We need the following text on our homepage:

"Immer der beste Preis -
denn Reisebüros kämpfen um Sie!"
(means "Always the best rate - as travel agents compete offer the best deal")
This is a sort of headline.

We also need:

So funktioniert Wellenfuchsportal:
1. Wunschkreuzfahrt wählen
2. Angebote erhalten und vergleichen
3. Reisebüro kontaktieren und buchen

(This explains briefly how our system works.)

Aside banners maybe needed later for advertising.

Additions I need on the front page are:
- Login / Sign-Up / Your benefits
(I quite like the way it's done on http://www.lirmatimes.com, at the very top of the page)
- Recommendation-link
(for everything else: Pls. refer to wfp02.wellenfuchsportal.de
- 3 or 4 "top offers of the week"
(current format is not very appealing; offers can be displayed as on http://sailings.tripnuvo.com/affiliate/promo.rvlx?OfferID=DOLUMA27 or

A maritime look is surely an option here, as we focus on cruises. But maybe you can surprise me with a great idea.

I quite like the designs where basically one photo / picture is used.
Some examples which look great IMHO:
http://pell-works.artfolioz.com/art/Glint-Swimmers-519304826
http://quorvanwebdesign.artfolioz.com/art/Website-Design-736152940
The following designer has also done a great job:
http://pixelmaker4387.artfolioz.com/gallery/

ATTACHED:
- logo
- Glint-Swimmers Design .png
- Flyer we use to attract travel agencies
- photo we use for the flyer (we own the rights)

Please get in touch with me if there are any questions or if you require further details. I ll get back to all inquiries / messages as soon as possible, usually within a few hours... Feel free to ask technical questions, too, (if any), the developer will be of assistance.

Reason: I decided to extend the deadline to have more time to comment on your designs and allow you to submit a few more proposals.

Reason: Sorry, more time needed to comment on all designs. Apart from this, some designers asked for more time.

Dear All,

Thank you so much for all your proposals.
Later today I will have a decent internet connection connection again, so I will be able to finally comment on your ideas and visions.

Hopefully next week we can finalize this project. Feel free to submit more designs or ask any questions if there are any.
Remember: Wellenfuchsportal won't be an ordinary travel agent. It brings cruise holiday makers and travel agents together.

Best

Target Market(s)

Holidaymakers / potential cruise holiday makers between 20 and 80.

Industry/Entity Type

Advertising

Requirements
Should not have
• Design should not use old-style, serif fonts.

```html
<!DOCTYPE html>
<html lang="de">
<head>
<meta charset="utf-8">
<title>Wellenfuchsportal – Kreuzfahrt Preisvergleich</title>
<link href="https://fonts.googleapis.com/css2?family=PT+Sans:wght@400;700&display=swap" rel="stylesheet">
<style>
:root{
  --sky-top:#5d8fc6;
  --sky-mid:#a9c8e6;
  --sea-deep:#1d3f6e;
  --sea:#3c6a9e;
  --navy:#1f3f6a;
  --brand-blue:#2a5d96;
  --brand-orange:#f29420;
  --panel:rgba(255,255,255,.38);
  --white:#ffffff;
  --text:#3a3a3a;
  --muted:#5e5e5e;
  --btn-navy:#1c3a63;
  --deck:#b79a7c;
  --rule:#f0a53a;
  --link-red:#c0392b;
}
*{box-sizing:border-box;margin:0;padding:0}
html,body{width:698px;height:1200px;overflow:hidden}
body{font-family:"PT Sans",Arial,sans-serif;color:var(--text);position:relative;
  background:linear-gradient(180deg,var(--sky-top) 0%,var(--sky-mid) 30%,#6d95c0 48%,var(--sea) 62%,var(--sea-deep) 80%,var(--deck) 92%,#9c7f62 100%)}
.abs{position:absolute}
/* top bar */
.topbar{top:28px;left:33px;font-size:8px;color:#111;display:flex;gap:12px;align-items:center}
.topbar a{color:var(--white);text-decoration:none;display:flex;align-items:center;gap:3px;font-size:7px}
.topbar .dot{width:9px;height:9px;border-radius:50%;background:#dfe8f2;display:inline-block}
.search{top:20px;left:536px;width:129px;height:16px;background:#fff;border-radius:4px;border:1px solid #c9c9c9;font-size:6px;color:#aaa;padding:4px 0 0 14px}
.search span{position:absolute;right:0;top:0;width:22px;height:14px;background:var(--brand-orange);border-radius:0 3px 3px 0}
/* panel */
.panel{top:46px;left:29px;width:640px;height:1042px;background:var(--panel);box-shadow:0 0 4px rgba(0,0,0,.25)}
.brand{top:66px;left:52px;display:flex;align-items:center;gap:10px}
.brand .mark{width:60px;height:60px;border-radius:50%;background:var(--brand-blue)}
.brand .name{font-size:19px;color:var(--brand-blue);letter-spacing:.5px;line-height:1.1}
.call{top:73px;left:536px;display:flex;gap:6px;color:var(--navy)}
.call small{display:block;font-size:10px}
.call b{font-weight:400;font-size:13px}
.nav{top:146px;left:29px;width:640px;height:26px;background:linear-gradient(#fff,#ececec);display:flex;font-size:8px;color:#111}
.nav span{padding:9px 10px 0;border-right:1px solid #ddd;height:26px}
.hero{top:172px;left:29px;width:640px;height:272px;background:linear-gradient(180deg,#c8ddf0 0%,#9fbfe0 35%,#2c5d94 55%,#163b6c 100%)}
.hero h1{position:absolute;top:114px;left:14px;font-weight:400;font-size:13.5px;color:#fff;line-height:1.5}
.dots{position:absolute;right:24px;bottom:14px;display:flex;gap:3px}
.dots i{width:5px;height:5px;border-radius:50%;background:#cfd7e0}
.dots i.on{background:#fff}
/* newsletter */
.news{top:466px;left:39px;width:180px;height:120px;background:#fff;border-radius:3px;padding:8px 10px;font-size:6.5px}
.news h3{font-weight:400;font-size:10px;color:#111;margin-bottom:7px}
.news .field{height:15px;border:1px solid #ddd;border-radius:3px;background:#f1f1f1;margin:3px 0 8px}
.news button{position:absolute;right:10px;bottom:8px;width:47px;height:16px;border:0;border-radius:3px;background:var(--btn-navy);color:#fff;font:8px "PT Sans",sans-serif}
.welcome{top:465px;left:246px;width:410px;font-size:6.3px;line-height:1.9;color:#111}
.welcome h2{font-weight:400;font-size:12px;margin-bottom:5px;color:#111}
.welcome p{margin-bottom:10px}
.more{top:588px;left:610px;font-size:6.5px;color:var(--link-red)}
.section-title{font-size:16px;color:var(--navy);font-weight:400;letter-spacing:-.2px;border-bottom:1px dotted #999;padding-bottom:4px}
/* steps */
.step{top:638px;width:167px;height:144px;background:#fff;padding:10px 10px;overflow:hidden;clip-path:polygon(0 0,92% 0,100% 8%,100% 100%,0 100%)}
.step h4{font-weight:400;font-size:9.5px;color:#111;line-height:1.3}
.step h4 em{font-style:normal;color:var(--brand-blue);display:block}
.step p{font-size:6.4px;line-height:1.65;color:var(--muted);margin-top:6px}
.step .num{position:absolute;right:-8px;bottom:-8px;width:50px;height:50px;border-radius:50%;background:var(--brand-blue);color:#fff;font-size:14px;padding:15px 0 0 16px}
/* offers */
.offer{top:854px;width:168px;height:214px;background:#fff;padding:7px}
.offer .photo{height:74px;background:linear-gradient(180deg,#7fb3dd 0%,#e8eef3 55%,#2e6aa0 100%)}
.offer .date{font-size:7px;color:var(--brand-blue);margin-top:9px}
.offer .route{font-size:6px;color:var(--brand-blue);margin-top:5px}
.offer .line{font-size:6px;color:var(--muted);margin-top:5px}
.prices{display:flex;justify-content:space-around;border-top:1px solid var(--rule);border-bottom:1px solid var(--rule);margin:6px -7px 0;padding:4px 0;font-size:6.4px;color:#333}
.prices small{display:block;font-size:5.5px;color:#666;margin-bottom:3px}
.offer .perk{font-size:6px;color:var(--muted);margin:6px 4px 0;width:100px;line-height:1.6}
.offer .select{position:absolute;right:14px;bottom:6px;width:78px;height:17px;border-radius:3px;background:linear-gradient(#ffa21c,#ef7b05);color:#111;font-size:7px;text-align:center;padding-top:4px}
/* footer */
.footer{top:1106px;left:29px;width:640px;height:86px;background:rgba(255,255,255,.4);font-size:6.2px;color:#111;padding:10px 0 0 23px}
.fcol{position:absolute;top:10px;line-height:1.7}
.fcol h5{font-weight:400;font-size:7px;margin-bottom:8px}
.social{position:absolute;top:8px;left:548px;display:flex;gap:8px}
.social i{width:13px;height:13px;background:var(--brand-blue);display:block}
.social i:last-child{background:var(--brand-orange)}
.copy{position:absolute;top:40px;left:489px;text-align:right;width:140px;line-height:2}
</style>
</head>
<body>
<div class="abs topbar">Offers and Requests Set Free
  <a><i class="dot"></i>Login</a><a><i class="dot"></i>Sign-Up</a><a><i class="dot"></i>Your benefits</a></div>
<div class="abs search">Search<span></span></div>

<div class="abs panel"></div>
<div class="abs brand"><span class="mark"></span><div class="name">WELLENFUCHS<br>PORTAL</div></div>
<div class="abs call">
  <svg width="18" height="30" viewBox="0 0 18 30"><path d="M4 2h5l1 7-4 2c1 4 2 7 4 9l4-2 3 6-4 3C7 27 2 18 1 8z" fill="#1b1b1b"/></svg>
  <div><small>Call Now</small><b>02931 - 508624</b></div>
</div>
<div class="abs nav"><span>So Gehts</span><span>Angebote erhalten</span><span>Kreuzfahrtsuche</span><span>Reedereien und Schiffe</span><span>Specials</span><span>Kontakt</span><span>Fehlermeldung</span><span style="border:0">Trac</span></div>
<div class="abs hero" role="img" aria-label="Kreuzfahrtschiff auf offenem Meer vor Küste">
  <h1>Immer der beste Preis -<br>denn Reisebüros kämpfen um Sie!</h1>
  <div class="dots"><i></i><i></i><i class="on"></i><i></i><i></i></div>
</div>

<div class="abs news">
  <h3>Subscribe Our Newsletter</h3>
  Enter the your name<div class="field"></div>
  Enter the your Email id<div class="field"></div>
  <button>Submit</button>
</div>
<div class="abs welcome">
  <h2>Welcome to WELLENFUCHSPORTAL</h2>
  <p>Lorem ipsum dolor sit amet, consectetur adipiscing elit. Lorem ipsum dolor sit amet, consectetur adipiscing elit. Lorem ipsum dolor sit amet, consectetur adipiscing elit. Loremipsum dolor sit amet, consectetur adipiscing elit. Lorem ipsum dolor sit amet, consectetur adipiscing elit. Lorem ipsum dolor sit amet, consectetur adipiscing elit. Lorem ipsum dolor sit amet, consectetur adipiscing elit.</p>
  <p>consectetur adipiscing elit. Loremipsum dolor sit amet, consectetur adipiscing elit. Lorem ipsum dolor sit amet, consectetur adipiscing elit. Lorem ipsum dolor sit amet, consectetur adipiscing elit. Lorem ipsum dolor sit amet, consectetur adipiscing elit. Lorem ipsum dolor sit amet, consectetur adipiscing elit.</p>
</div>
<div class="abs more">View More &gt;&gt;</div>

<h2 class="abs section-title" style="top:602px;left:42px;width:200px">HOW THE SYSTEM WORKS</h2>
<div class="abs step" style="left:43px"><h4>WUNSCHKREUZF<em>AHRT WAHLEN</em></h4>
  <p>Lorem ipsum dolor sit amet, consectetur adipiscing elit. Lorem ipsum dolor sit amet, consectetur adipiscing elit. Lorem ipsum dolor sit adipiscing elit.</p>
  <p>Loremipsum dolor sit amet, consectetur adipiscing elit. Lorem ipsum dolor sit amet, consectetur adipiscing elit.</p><span class="num">1</span></div>
<div class="abs step" style="left:247px"><h4>ANGEBOTE<em>ERHALTEN UND VERGLEICHEN</em></h4>
  <p>Lorem ipsum dolor sit amet, consectetur adipiscing elit. Lorem ipsum dolor sit amet, consectetur adipiscing elit. Lorem ipsum dolor sit adipiscing elit.</p>
  <p>Loremipsum dolor sit amet, consectetur adipiscing elit. Lorem ipsum dolor sit amet, consectetur adipiscing elit.</p><span class="num">2</span></div>
<div class="abs step" style="left:463px"><h4>REISEBURO<em>KONTACKTIEREN UND BUCHEN</em></h4>
  <p>Lorem ipsum dolor sit amet, consectetur adipiscing elit. Lorem ipsum dolor sit amet, consectetur adipiscing elit. Lorem ipsum dolor sit adipiscing elit.</p>
  <p>Loremipsum dolor sit amet, consectetur adipiscing elit. Lorem ipsum dolor sit amet, consectetur adipiscing elit.</p><span class="num">3</span></div>

<h2 class="abs section-title" style="top:812px;left:42px;width:320px">THE 3 BEST OFFERS OF THE WEEK / MONTH</h2>
<div class="abs offer" style="left:45px">
  <div class="photo" role="img" aria-label="Kreuzfahrtschiff auf türkisem Wasser"></div>
  <div class="date">NOV 16 2012</div><div class="route">10 DAY EASTERN CARIBBEAN FROM MIAMI</div><div class="line">Nordlicht Cruise Line - Nordlicht Aura</div>
  <div class="prices"><div><small>INSIDE.</small>€ 2.899</div><div><small>BALCONY</small>€ 310</div><div><small>SUITE</small>€ 336</div></div>
  <div class="perk">Free bottle of sparkline wine and chocolate strawberries</div><div class="select">SELECT</div></div>
<div class="abs offer" style="left:254px">
  <div class="photo" role="img" aria-label="Kreuzfahrtschiff auf blauem Meer"></div>
  <div class="date">NOV 16 2012</div><div class="route">10 DAY EASTERN CARIBBEAN FROM MIAMI</div><div class="line">Nordlicht Cruise Line - Nordlicht Aura</div>
  <div class="prices"><div><small>INSIDE.</small>€ 2.899</div><div><small>BALCONY</small>€ 310</div><div><small>SUITE</small>€ 336</div></div>
  <div class="perk">Free bottle of sparkline wine and chocolate strawberries</div><div class="select">SELECT</div></div>
<div class="abs offer" style="left:464px">
  <div class="photo" role="img" aria-label="Bug eines Kreuzfahrtschiffs im Hafen" style="background:linear-gradient(180deg,#8fb6dc 0%,#f1ede4 50%,#b9a78f 100%)"></div>
  <div class="date">NOV 16 2012</div><div class="route">10 DAY EASTERN CARIBBEAN FROM MIAMI</div><div class="line">Nordlicht Cruise Line - Nordlicht Aura</div>
  <div class="prices"><div><small>INSIDE.</small>€ 2.899</div><div><small>BALCONY</small>€ 310</div><div><small>SUITE</small>€ 336</div></div>
  <div class="perk">Free bottle of sparkline wine and chocolate strawberries</div><div class="select">SELECT</div></div>

<footer class="abs footer">
  <div class="fcol" style="left:23px"><h5>ABOUT US</h5>About Wellenfuchsportal.de<br>Jobs<br>Partner<br>Advertise Wellenfuchsportal.de</div>
  <div class="fcol" style="left:157px"><h5>PRESS</h5>Press material<br>Wellenfuchs in the media<br>Press Releases<br>Wellenfuchs and the social media</div>
  <div class="fcol" style="left:297px"><h5>HELP &amp; SERVICE</h5>Product Reviews<br>Contact<br>FAQ's</div>
  <div class="fcol" style="left:402px"><h5>DISCLAIMER</h5>Disclaimer / disclaimer<br>Terms of Service<br>Imprint</div>
  <div class="social"><i></i><i></i><i></i><i></i></div>
  <div class="copy">© 2012 .wellenfuchsportal.de| All right reserved<br>x2</div>
</footer>
</body>
</html>
```